Naturopath needs product label for new essence range

I need a label design for a new range of Essences. The essences resonate with the energetic chakra centres of the body to shift blockages, balance them and lead to transformation and spiritual growth. I have a logo to be used. The name of the essence range is Corvanthe which means "to reveal truth or True Nature". The first essence resonates with the Base Chakra and is called "Base" I would like a strong bold red colour to feature in the design. The label size would be about 76mm x 27mm. See below for the required information to be on the label.
Updates

Hi everyone, I'm not sure if it's important to help with the design, but I've just uploaded the logo in several different formats. Thanks for all your submissions. Also please use a deep red colour, the example from the colour wheel is too light. Kind regards, Dorian

Target Market(s)

Adults open to alternative therapies and spiritual development

Industry/Entity Type

Product

Colors
eb1f27

Requirements
Must have
• The logo. A deep red colour as the background or part of the background
"Base"
corvantheessences.example.au
Batch
Expiry
Ingredients: vibrational essence of herbs, flowers and crystals, purified water, brandy (approx 12.5% alcohol)
20ml
Dosage: 7 drops once a day

```html
<!DOCTYPE html>
<html lang="en">
<head>
<meta charset="utf-8">
<title>Corvanthe Essences – Base label</title>
<link rel="stylesheet" href="https://fonts.googleapis.com/css2?family=Cinzel:wght@400;500&family=Montserrat:wght@400;600&display=swap">
<style>
  :root {
    --page: #ffffff;
    --red: #eb1f27;
    --ink-dark: #0e0607;
    --maroon: #5e0a0f;
    --gold: #d9a441;
    --gold-light: #f3cf6d;
    --white: #ffffff;
  }
  * { margin: 0; padding: 0; box-sizing: border-box; }
  html, body { width: 1200px; height: 1200px; overflow: hidden; background: var(--page); }
  .canvas { position: relative; width: 1200px; height: 1200px; }

  .label {
    position: absolute; left: 388px; top: 56px; width: 381px; height: 1076px;
    background: var(--red); overflow: hidden;
  }
  .ribbon { position: absolute; left: 90px; top: 0; width: 202px; height: 338px; }
  .brand-mark {
    position: absolute; left: 117px; top: 180px; width: 148px; height: 148px;
    display: flex; align-items: center; justify-content: center;
    border: 3px solid var(--gold); border-radius: 50%;
    font-family: "Cinzel", serif; font-weight: 500; font-size: 17px;
    color: var(--gold); letter-spacing: 1px;
  }

  .title-block { position: absolute; left: 0; top: 390px; width: 100%; text-align: center; color: var(--white); }
  .range-name {
    font-family: "Cinzel", serif; font-weight: 400; font-size: 40px;
    letter-spacing: 3px; line-height: 1;
  }
  .range-sub {
    margin-top: 8px; display: flex; align-items: center; justify-content: center; gap: 12px;
    font-family: "Cinzel", serif; font-size: 21px; letter-spacing: 3px; line-height: 1;
  }
  .range-sub .rule { width: 72px; height: 2px; background: linear-gradient(90deg, transparent, var(--gold-light), var(--gold), transparent); }
  .product-name {
    margin-top: 2px; font-family: "Cinzel", serif; font-weight: 500; font-size: 108px;
    letter-spacing: 4px; line-height: 1;
  }
  .divider {
    width: 290px; height: 2px; margin: 0 auto;
    background: linear-gradient(90deg, transparent, var(--gold), var(--gold-light), var(--gold), transparent);
  }
  .divider.top { margin-top: 20px; }
  .web {
    font-family: "Montserrat", sans-serif; font-size: 17px; letter-spacing: 0.5px;
    padding: 13px 0 12px;
  }
  .volume { margin-top: 44px; font-family: "Montserrat", sans-serif; font-size: 19px; letter-spacing: 1px; }

  .info-panel {
    position: absolute; left: 0; top: 754px; width: 100%; height: 322px;
    background: linear-gradient(90deg, var(--ink-dark) 0%, var(--maroon) 40%, #3a0a0b 60%, var(--maroon) 78%, var(--ink-dark) 100%);
    color: var(--white); font-family: "Montserrat", sans-serif; font-size: 15px; line-height: 18px;
    padding: 30px 20px 0 49px; letter-spacing: 0.4px;
  }
  .info-panel h3 { font-size: 15px; font-weight: 600; letter-spacing: 1px; }
  .info-panel p { margin-bottom: 22px; }
  .info-panel .dose { margin-bottom: 28px; }
  .info-panel .field { font-weight: 600; letter-spacing: 1px; margin-bottom: 12px; }
</style>
</head>
<body>
<div class="canvas">
  <div class="label">
    <svg class="ribbon" viewBox="0 0 202 338" aria-hidden="true">
      <defs>
        <linearGradient id="ribbonShade" x1="0" x2="1" y1="0" y2="0">
          <stop offset="0" stop-color="#0e0607"/>
          <stop offset="0.45" stop-color="#6a0b12"/>
          <stop offset="0.6" stop-color="#3a0a0b"/>
          <stop offset="1" stop-color="#0e0607"/>
        </linearGradient>
      </defs>
      <path d="M0 0 H202 V326 Q101 350 0 326 Z" fill="url(#ribbonShade)"/>
    </svg>
    <div class="brand-mark">Corvanthe</div>

    <div class="title-block">
      <div class="range-name">CORVANTHE</div>
      <div class="range-sub"><span class="rule"></span>Essences<span class="rule"></span></div>
      <div class="product-name">BASE</div>
      <div class="divider top"></div>
      <div class="web">corvantheessences.example.au</div>
      <div class="divider"></div>
      <div class="volume">20ml</div>
    </div>

    <div class="info-panel">
      <h3>Ingredients:</h3>
      <p>vibrational essence of herbs, flowers and crystals, purified water, brandy (approx 12.5% alcohol)</p>
      <h3>Dosage:</h3>
      <p class="dose">7 drops once a day</p>
      <div class="field">Batch:</div>
      <div class="field">Expiry:</div>
    </div>
  </div>
</div>
</body>
</html>
```